Traffic product supplier - Temporary Raised Pavement Markers

We need a flyer design that will grab the customer's eye to the product (TRPMs) and entice curiosity to the business. Showing 1 product but promoting other products. The following information should be included:
- Logo (attached)
- Sale Product image (Temporary Road Pavement Marker AKA Press and Holds)
- Product wording (attached word document)

Happy for you to add/amend wording for grammatical purpose and other images that show it is a sale flyer.

Background on KLV - We are a thermoplastic manufacturer for road markings and traffic product supplier. KLV specializes in producing high quality hotmelt thermoplastic that meet Australian Standard AS4049.2. We are able to produce other specifications as required by the customer.

Would like the colour scheme to be similar to the logo.

If you need more information let me know.

Target Market(s)

Asphalt industry / road builders

Font styles to use
Serif
Sans Serif

Requirements
Must have
• - Kelvoro Lane Ventures (My company name)
- Contact details:
- 02 8417 2530
- marcus.t@klvsupplyco.com.au
- info@klvsupplyco.com.au
-www.klvmtq.com

- Attached images.
-Title (Temporary Road Pavement Markers)

```html
<!DOCTYPE html>
<html lang="en">
<head>
<meta charset="utf-8">
<title>KLV – Temporary Raised Pavement Markers</title>
<link href="https://fonts.googleapis.com/css2?family=Oswald:wght@500;600&family=Open+Sans:ital,wght@0,400;0,600;1,600;1,700&display=swap" rel="stylesheet">
<style>
  :root{
    --blue:#1a5ba9;
    --blue-deep:#114d96;
    --yellow:#f6c21c;
    --yellow-shade:#d9a70f;
    --panel:#eaf2fb;
    --ink:#3c4350;
    --page:#ffffff;
    --backdrop:#ececec;
  }
  *{margin:0;padding:0;box-sizing:border-box}
  html,body{width:1200px;height:915px;overflow:hidden;background:var(--backdrop)}
  .flyer{
    position:absolute;left:281px;top:6px;width:596px;height:843px;
    transform:scale(1.07);transform-origin:0 0;
    background:var(--page);overflow:hidden;
    font-family:"Open Sans",Arial,sans-serif;
    box-shadow:0 2px 8px rgba(0,0,0,.18);
  }
  .hero-photo{
    position:absolute;left:0;top:0;width:596px;height:330px;
    background:linear-gradient(180deg,#b9cde0 0%,#dfe6ea 30%,#a79c7a 38%,#8c8a78 52%,#c9cbcd 70%,#e8eaec 100%);
  }
  .product-photo{
    position:absolute;left:110px;top:130px;width:355px;height:140px;
    background:linear-gradient(90deg,#e0b52c 0%,#e0b52c 28%,#e9e9e9 30%,#dcdfe3 100%);
    opacity:.9;border-radius:3px;
  }
  .title{
    position:absolute;top:30px;left:0;width:596px;text-align:center;
    font-family:"Oswald",sans-serif;font-weight:600;font-size:34px;color:var(--blue);
    letter-spacing:.2px;
  }
  .bands{position:absolute;left:0;top:285px}
  .offer-label{
    position:absolute;top:294px;left:330px;width:266px;text-align:center;
    font-family:"Oswald",sans-serif;font-weight:500;font-size:19px;color:#fff;letter-spacing:.5px;
  }
  .offer-label .rule{display:inline-block;width:20px;height:8px;vertical-align:middle;margin:0 8px;
    background:repeating-linear-gradient(180deg,var(--yellow) 0 2px,transparent 2px 3px)}
  .colour-note{
    position:absolute;top:336px;left:30px;font-style:italic;font-weight:600;font-size:11.5px;color:#fff;
  }
  .brand{position:absolute;left:26px;top:395px;display:flex;align-items:center;gap:10px}
  .brand-mark{width:34px;height:34px;background:var(--yellow)}
  .brand-name{font-family:"Oswald",sans-serif;font-weight:600;font-size:48px;color:var(--blue);line-height:1}
  .thumbs{
    position:absolute;left:292px;top:370px;width:288px;height:66px;
    background:linear-gradient(90deg,#e2b02a 0 30%,#fff 30% 35%,#e7e7e7 35% 64%,#fff 64% 69%,#e5e6e8 69%);
  }
  .intro{position:absolute;left:20px;top:506px;width:255px;color:var(--blue)}
  .intro h2{font-family:"Oswald",sans-serif;font-weight:600;font-size:18.5px;line-height:23px;margin-bottom:6px}
  .intro p{font-size:10.8px;line-height:14.4px;text-align:justify;margin-bottom:14px}
  .phone{position:absolute;left:36px;top:692px;display:flex;align-items:center;gap:10px;
    font-family:"Oswald",sans-serif;font-weight:500;font-size:27px;color:var(--blue)}
  .phone-note{position:absolute;left:34px;top:730px;font-size:11px;font-style:italic;font-weight:600;color:var(--blue)}
  .details{position:absolute;left:288px;top:472px;width:294px;height:318px;background:var(--panel);
    padding:24px 12px 0 12px;color:var(--ink)}
  .details p{font-size:10.6px;line-height:14.4px;text-align:justify}
  .specs{list-style:none;margin-top:20px}
  .specs li{position:relative;padding-left:22px;font-size:11px;line-height:13.5px;margin-bottom:11px}
  .specs svg{position:absolute;left:0;top:1px}
  .price-tag{position:absolute;left:298px;top:762px}
  .price-text{position:absolute;left:300px;top:766px;width:270px;text-align:center;
    font-family:"Oswald",sans-serif;font-weight:600;font-size:20px;color:#fff}
  .footer{position:absolute;left:0;top:765px}
  .contacts{position:absolute;left:22px;top:780px;list-style:none;color:#fff;font-size:12.5px;line-height:18.5px}
  .contacts li{display:flex;align-items:center;gap:6px}
  .contacts .dot{width:12px;height:12px;border-radius:50%;background:var(--yellow);display:inline-block}
</style>
</head>
<body>
<div class="flyer">
  <div class="hero-photo" role="img" aria-label="Straight country road through grassland under a cloudy sky">
    <div class="product-photo" role="img" aria-label="Yellow, red-strip and white temporary raised pavement markers standing on the road"></div>
  </div>
  <h1 class="title">Temporary Raised Pavement Markers</h1>

  <svg class="bands" width="596" height="80" viewBox="0 0 596 80" aria-hidden="true">
    <path d="M300 2 H596 V40 H286 Z" fill="var(--blue)"/>
    <path d="M0 40 H286 L268 76 Q264 80 256 80 H0 Z" fill="var(--blue)"/>
  </svg>
  <div class="offer-label"><span class="rule"></span>SPECIAL OFFER<span class="rule"></span></div>
  <div class="colour-note">Available in all white, red and blue!</div>

  <div class="brand"><span class="brand-mark"></span><span class="brand-name">KLV</span></div>

  <div class="thumbs" role="img" aria-label="Three pavement markers: yellow, white with red strip, white with blue strip"></div>

  <section class="intro">
    <h2>Temporary Road Pavement<br>Marker AKA Press and Holds</h2>
    <p>Temporary road pavement markers, also known as press ‘n’ holds, are a great short-term solution to mark asphalt and pavements before permanent line marking takes place.</p>
    <p>They provide a way to delineate lanes and edges before the permanent longitudinal line marking process takes place.</p>
  </section>

  <div class="phone">
    <svg width="26" height="28" viewBox="0 0 26 28" aria-hidden="true"><rect x="7" y="1" width="15" height="26" rx="3" fill="var(--blue)"/><rect x="10" y="5" width="9" height="15" fill="#fff"/><path d="M7 8 Q1 14 7 20" stroke="var(--blue)" stroke-width="3" fill="none"/></svg>
    <span>02 8417 2530</span>
  </div>
  <div class="phone-note">for more information please contact us</div>

  <section class="details">
    <p>TRPMs or press ‘n’ holds are available in yellow or white and come with a Class 1A reflective strip applied to tough high impact plastic. They are an economical solution for making newly laid roads safer. An easy to remove clear cover protects the reflective film during sealing and is easily ripped off afterwards.</p>
    <ul class="specs">
      <li><svg width="12" height="12" viewBox="0 0 12 12"><circle cx="6" cy="6" r="6" fill="var(--blue)"/><path d="M3.3 6.2 5.2 8 8.7 4.2" stroke="#fff" stroke-width="1.5" fill="none"/></svg>Dimensions:<br>100 mm long x 50 mm high x 25 mm wide</li>
      <li><svg width="12" height="12" viewBox="0 0 12 12"><circle cx="6" cy="6" r="6" fill="var(--blue)"/><path d="M3.3 6.2 5.2 8 8.7 4.2" stroke="#fff" stroke-width="1.5" fill="none"/></svg>Double sided Class 1A Reflective</li>
      <li><svg width="12" height="12" viewBox="0 0 12 12"><circle cx="6" cy="6" r="6" fill="var(--blue)"/><path d="M3.3 6.2 5.2 8 8.7 4.2" stroke="#fff" stroke-width="1.5" fill="none"/></svg>Clear cover for reflective protection</li>
      <li><svg width="12" height="12" viewBox="0 0 12 12"><circle cx="6" cy="6" r="6" fill="var(--blue)"/><path d="M3.3 6.2 5.2 8 8.7 4.2" stroke="#fff" stroke-width="1.5" fill="none"/></svg>Available in all white, and red (reflective strip)<br>&nbsp;and white, all yellow and all blue</li>
    </ul>
  </section>

  <svg class="price-tag" width="284" height="42" viewBox="0 0 284 42" aria-hidden="true">
    <path d="M6 4 H266 L280 38 H2 Z" fill="var(--yellow-shade)"/>
    <path d="M2 0 H262 L276 34 H0 Z" fill="var(--yellow)"/>
  </svg>
  <div class="price-text">$0.40 ex GST per TRPM</div>

  <svg class="footer" width="596" height="78" viewBox="0 0 596 78" aria-hidden="true">
    <path d="M0 6 H262 C282 6 286 46 312 46 H596 V78 H0 Z" fill="var(--blue)"/>
  </svg>
  <ul class="contacts">
    <li><span class="dot"></span>info@klvsupplyco.com.au</li>
    <li><span class="dot"></span>marcus.t@klvsupplyco.com.au</li>
    <li><span class="dot"></span>www.klvmtq.com</li>
  </ul>
</div>
</body>
</html>
```